New label design for Vitmain Water beverage

This is to create a new label for a vitamin water company called Kerun Vitamin. The label should be in dual languages. English and Arabic as seen attached for a previous example. You do not have to create an Arabic logo, just make space for it and I will have someon else do it. If you think you can do it, go ahead. I have also attached the bottle dimensions we are thinking of using. Please provide a new bottle design if you see fit. Please remember the bottle size is 400ml, and no pressure If I don't get a great bottle design, then I will use the attached one in that case. Please make the label diverse for various flavors, so it would apply easily and color print friendly. The brand is healthy, sporty, low or no sugars, no artificial flavors and no artificial coloring. All vitamins, minirals and electrolytes are healthy and real. Three flavors: pomogranite cherry, tropical citrus, and kiwi strawberry. So, each label would have different vitamins and offers unique components. Make it hip, trendy yet classy.
Good Luck!!!
Updates

Project Deadline Extended Reason: Because I updated a new file image example to follow and innovate from. Added Monday, February 02, 2015

Posted new file image example to follow and innovate from. Thanks, Added Monday, February 02, 2015

Target Market(s)

Age 15-40 males and females

Industry/Entity Type

Water Company

Requirements
Nice to have
• Plastic PET bottle design
• a 500 ml version

```html
<!DOCTYPE html>
<html lang="en">
<head>
<meta charset="utf-8">
<title>Kerun Vitamin – Flavour Labels</title>
<link rel="stylesheet" href="https://fonts.googleapis.com/css2?family=Varela+Round&family=Oswald:wght@400;500&display=swap">
<style>
  :root{
    --canvas:#ffffff;
    --label-white:#ffffff;
    --label-silver:#e4e5e8;
    --ink-light:#ffffff;
    --kiwi:#7b1f5e;
    --kiwi-soft:#c2619a;
    --pom-dark:#b3182c;
    --pom-dark-soft:#e0606c;
    --citrus:#eea51c;
    --citrus-soft:#f7cf6e;
    --pom-bright:#d51f42;
    --pom-bright-soft:#ef7488;
  }
  *{box-sizing:border-box;margin:0;padding:0}
  html,body{width:1200px;height:744px;overflow:hidden;background:var(--canvas)}
  .label-row{
    position:relative;width:1200px;height:744px;
    display:flex;justify-content:center;align-items:center;gap:30px;
  }
  .label{
    --accent:var(--kiwi);--accent-soft:var(--kiwi-soft);
    position:relative;width:255px;height:360px;overflow:hidden;
    background:linear-gradient(90deg,var(--label-silver) 0%,var(--label-white) 22%,var(--label-white) 78%,var(--label-silver) 100%);
    box-shadow:0 0 0 1px #d9dadd;
  }
  .label--kiwi{--accent:var(--kiwi);--accent-soft:var(--kiwi-soft)}
  .label--pom-dark{--accent:var(--pom-dark);--accent-soft:var(--pom-dark-soft)}
  .label--citrus{--accent:var(--citrus);--accent-soft:var(--citrus-soft)}
  .label--pom-bright{--accent:var(--pom-bright);--accent-soft:var(--pom-bright-soft)}

  .natural-badge{
    position:absolute;left:12px;top:14px;width:58px;height:46px;
    background:var(--accent);border-radius:10px 10px 10px 2px;
    color:var(--ink-light);font-family:"Varela Round",sans-serif;
    font-size:12px;line-height:1.05;text-align:center;padding-top:9px;
  }
  .natural-badge small{display:block;font-size:8.5px;letter-spacing:.3px}

  .splash-art{
    position:absolute;right:12px;top:8px;width:96px;height:150px;
    border-radius:40% 60% 30% 70% / 50% 40% 60% 50%;
    background:radial-gradient(circle at 60% 35%,var(--accent-soft),var(--accent) 75%);
    opacity:.85;
  }

  .brand{
    position:absolute;left:0;right:0;top:70px;text-align:center;
    font-family:"Varela Round",sans-serif;color:var(--accent);line-height:.95;
  }
  .brand-name{display:block;font-size:58px;letter-spacing:-1px}
  .brand-line{display:block;font-size:36px;margin-top:2px}

  .flavour-band{
    position:absolute;left:10px;right:10px;top:192px;height:28px;
    background:var(--accent);border:2px solid var(--ink-light);
    box-shadow:0 0 0 1px var(--accent);
    color:var(--ink-light);font-family:"Oswald",sans-serif;font-weight:500;
    font-size:15px;letter-spacing:.6px;text-align:center;line-height:24px;text-transform:uppercase;
  }
  .band-chevron{position:absolute;left:50%;top:226px;transform:translateX(-50%)}

  .claims-band{
    position:absolute;left:0;right:0;top:262px;height:66px;
    background:var(--accent);color:var(--ink-light);
    font-family:"Oswald",sans-serif;font-size:10.5px;letter-spacing:.3px;
    padding:14px 14px 0;line-height:1.75;text-transform:uppercase;
  }
  .claims-band .claim-line--indent{padding-left:26px}
</style>
</head>
<body>
<main class="label-row">

  <section class="label label--kiwi">
    <div class="natural-badge">100%<small>NATURAL</small></div>
    <div class="splash-art" role="img" aria-label="Kiwi strawberry juice splash illustration"></div>
    <h2 class="brand"><span class="brand-name">Kerun</span><span class="brand-line">Vitamin</span></h2>
    <div class="flavour-band">Kiwi Strawberry</div>
    <svg class="band-chevron" width="26" height="10" viewBox="0 0 26 10" aria-hidden="true"><path d="M1 1 L13 9 L25 1" fill="none" stroke="#c5c6ca" stroke-width="2"/></svg>
    <div class="claims-band">
      <p>• No sugars &nbsp;• No artificial flavors and</p>
      <p class="claim-line--indent">• No artificial coloring</p>
    </div>
  </section>

  <section class="label label--pom-dark">
    <div class="natural-badge">100%<small>NATURAL</small></div>
    <div class="splash-art" role="img" aria-label="Pomegranate cherry juice splash illustration"></div>
    <h2 class="brand"><span class="brand-name">Kerun</span><span class="brand-line">Vitamin</span></h2>
    <div class="flavour-band">Pomogranite Cherry</div>
    <svg class="band-chevron" width="26" height="10" viewBox="0 0 26 10" aria-hidden="true"><path d="M1 1 L13 9 L25 1" fill="none" stroke="#c5c6ca" stroke-width="2"/></svg>
    <div class="claims-band">
      <p>• No sugars &nbsp;• No artificial flavors and</p>
      <p class="claim-line--indent">• No artificial coloring</p>
    </div>
  </section>

  <section class="label label--citrus">
    <div class="natural-badge">100%<small>NATURAL</small></div>
    <div class="splash-art" role="img" aria-label="Tropical citrus juice splash illustration"></div>
    <h2 class="brand"><span class="brand-name">Kerun</span><span class="brand-line">Vitamin</span></h2>
    <div class="flavour-band">Tropical Citrus</div>
    <svg class="band-chevron" width="26" height="10" viewBox="0 0 26 10" aria-hidden="true"><path d="M1 1 L13 9 L25 1" fill="none" stroke="#c5c6ca" stroke-width="2"/></svg>
    <div class="claims-band">
      <p>• No sugars &nbsp;• No artificial flavors and</p>
      <p class="claim-line--indent">• No artificial coloring</p>
    </div>
  </section>

  <section class="label label--pom-bright">
    <div class="natural-badge">100%<small>NATURAL</small></div>
    <div class="splash-art" role="img" aria-label="Pomegranate cherry juice splash illustration"></div>
    <h2 class="brand"><span class="brand-name">Kerun</span><span class="brand-line">Vitamin</span></h2>
    <div class="flavour-band">Pomogranite Cherry</div>
    <svg class="band-chevron" width="26" height="10" viewBox="0 0 26 10" aria-hidden="true"><path d="M1 1 L13 9 L25 1" fill="none" stroke="#c5c6ca" stroke-width="2"/></svg>
    <div class="claims-band">
      <p>• No sugars &nbsp;• No artificial flavors and</p>
      <p class="claim-line--indent">• No artificial coloring</p>
    </div>
  </section>

</main>
</body>
</html>
```